New doctor needs elegant, whimsical Business Card Design

CHALLENGE: how to highlight gynaecological service (use of abstract cervix in logo?) in NON-VULGAR way + project an elegant, professional tone?

We need a business card design (incl logo) for a gynaecologist who is starting his private practice. The main area of service will be colposcopy - a diagnostic procedure using a microscope to look at the tissues of the cervix for any potentially cancerous cells.

STYLE: Classic, elegant, timeless look. Fairly simple, not too cluttered. Logo NOT to overpower name. Want to project a professional but approachable image - "gentleman". Not too "corporate" - whimsical, without becoming feminine.

COLOUR: soft colours - no clashing primary colours, nothing too "brash" or commercial.
White background/black lettering + 1 colour accent, pattern repeated throughout card, in both logo & text (refer to "mock-up example" image file)
The colour accent should be BLUE: a serene/calm but confident shade: eg. strong pastel blue, dark baby blue (NOT royal blue, navy, turquoise, aquamarine, etc)

TEXT: have a calligraphy feel (but not too fancy as to be difficult to read at a glance) or more italics/rounded edges kind of font (refer to refer to "mock-up example" image file)
- Contrast between NAME in more italic font Vs. rest of text in "straight" print (or vice versa)

LOGO:
1) something very similar to "The Wren Trust" logo (ref image attached) - an abstract, black line drawing of a woman's figure, with a single, coloured symbol. No detail in line drawing - NO head or arms - don't want it to be obviously women's figure - want it very stylised, abstract, fluid lines.

* The Wren Trust used a heart but we would like to use an another symbol in BLUE - maybe an abstract of a cervix? eg. the "triangle" shape symbol (see the image file of the Silver Thread Wellness Initiative - the symbol in the middle of the flower) OR the "donut" representation of the cervix (see notes below)

BUT - don't want the symbol exactly over the groin area, otherwise looks vulgar. Don't want it to look like bikini or genitals! Symbol should be incorporated into line drawing but NOT drawing direct attention to the groin. Maybe displaced to one side? Or further up the body? Open to your ideas

2) We are also open to any other ideas you may have, of stylistic/abstract designs based on:
- the image of a cervix (looks very similar to a pink donut - usually shown in medical shorthand as a tiny circle in the middle of a bigger circle.)
- the cervix with some cells within ? Some stylised version of cancer cells?
(please see attached selection of images for reference/inspiration)

2 main audiences: women (18 - 70) concerned about abnormal PAP smear, other gynae-issues, 2) GP's referring their patients to a gynae-specialist

Medical

• ONE side only - Reverse of business card must be kept blank for "Appointments" notes.

• NO "retro" American feel - nor anything 60's or 70's kind of feel. Don't want fonts that look too commercial or industrial/harsh.

Logo: NO obvious silhouettes/profiles of women (abstract is OK but not detail), NO female reproductive system (2 ovaries & uterus), no female symbol - as these are the usual cliches for gynaecologists.

DON'T want the symbol exactly over the groin area, otherwise looks vulgar. Don't want it to look like bikini or genitals! Symbol should be incorporated into line drawing but NOT drawing direct attention to the groin. Maybe displaced to one side? Or further up the body? Open to your ideas

```html
<!DOCTYPE html>
<html lang="en">
<head>
<meta charset="utf-8">
<title>Dr Martin Ashby – Business Card</title>
<link rel="stylesheet" href="https://fonts.googleapis.com/css2?family=Parisienne&family=PT+Sans+Narrow:wght@400;700&family=PT+Sans:ital@1&display=swap">
<style>
  :root {
    --backdrop: #e4e4e4;
    --card: #ffffff;
    --accent-blue: #4f8fb3;
    --rule-blue: #5a8db0;
    --ink-grey: #6b6b6b;
    --blush: #f6dbe5;
  }
  * { margin: 0; padding: 0; box-sizing: border-box; }
  html, body { width: 1200px; height: 1000px; overflow: hidden; }
  body {
    background: var(--backdrop);
    position: relative;
    font-family: "PT Sans Narrow", "Arial Narrow", sans-serif;
  }
  .card {
    position: absolute;
    left: 290px;
    width: 620px;
    height: 378px;
    background: var(--card);
    box-shadow: 0 2px 10px rgba(0,0,0,0.12);
    overflow: hidden;
  }
  .card--back { top: 100px; }
  .card--front { top: 522px; }

  /* Appointment side */
  .appointments__rules { position: absolute; inset: 0; }
  .appointments__header {
    position: absolute;
    left: 52px; right: 52px; top: 48px;
    display: flex;
    justify-content: space-between;
    align-items: baseline;
    line-height: 1;
  }
  .appointments__label {
    font-size: 15px;
    letter-spacing: 2px;
    color: var(--accent-blue);
  }
  .appointments__title {
    font-weight: 700;
    font-size: 16px;
    letter-spacing: 3px;
    color: var(--ink-grey);
  }
  .appointments__web {
    position: absolute;
    left: 0; right: 0; bottom: 20px;
    text-align: center;
    font-size: 18px;
    letter-spacing: 1.5px;
    color: var(--accent-blue);
  }

  /* Identity side */
  .accent-dot { position: absolute; left: 244px; top: 140px; }
  .address {
    position: absolute;
    left: 34px; top: 26px;
    font-family: "PT Sans", sans-serif;
    font-style: italic;
    font-size: 15px;
    line-height: 1.2;
    color: var(--accent-blue);
    text-align: center;
  }
  .contact {
    position: absolute;
    right: 30px; top: 80px;
    font-size: 17px;
    line-height: 1.15;
    letter-spacing: 0.5px;
    color: var(--accent-blue);
    text-align: right;
  }
  .identity {
    position: absolute;
    left: 0; right: 0; top: 212px;
    text-align: center;
  }
  .identity__name {
    font-family: "Parisienne", cursive;
    font-weight: 400;
    font-size: 62px;
    line-height: 1;
    color: var(--accent-blue);
  }
  .identity__role {
    margin-top: 4px;
    font-size: 21px;
    letter-spacing: 3px;
    color: var(--ink-grey);
  }
  .identity__credentials {
    margin-top: 10px;
    font-size: 18px;
    letter-spacing: 0.5px;
    color: var(--accent-blue);
  }
</style>
</head>
<body>

  <section class="card card--back" aria-label="Appointment side">
    <svg class="appointments__rules" width="620" height="378" viewBox="0 0 620 378" aria-hidden="true">
      <g stroke="var(--rule-blue)" stroke-width="1.2">
        <line x1="40" y1="78" x2="580" y2="78"/>
        <line x1="40" y1="116" x2="580" y2="116"/>
        <line x1="40" y1="154" x2="580" y2="154"/>
        <line x1="40" y1="192" x2="580" y2="192"/>
        <line x1="40" y1="230" x2="580" y2="230"/>
        <line x1="40" y1="268" x2="580" y2="268"/>
        <line x1="40" y1="306" x2="580" y2="306"/>
      </g>
    </svg>
    <div class="appointments__header">
      <span class="appointments__label">DATE</span>
      <h2 class="appointments__title">APPOINTMENTS</h2>
      <span class="appointments__label">TIME</span>
    </div>
    <p class="appointments__web">Ashbygyn.com.au</p>
  </section>

  <section class="card card--front" aria-label="Identity side">
    <svg class="accent-dot" width="130" height="130" viewBox="0 0 130 130" aria-hidden="true">
      <circle cx="65" cy="65" r="62" fill="var(--blush)"/>
    </svg>
    <address class="address">
      Suite 12<br>
      Kestrel Medical Centre<br>
      40 Larch Ave<br>
      Fernhill, WA 6100
    </address>
    <p class="contact">
      T +61 8 6000 0142<br>
      F +61 8 6000 0143<br>
      admin@ashbygyn.com.au
    </p>
    <div class="identity">
      <h1 class="identity__name">Dr Martin Ashby</h1>
      <p class="identity__role">GYNAECOLOGIST</p>
      <p class="identity__credentials">MB BCh - MA(Oxon) - Dip Obs - FRANZCOG - MD</p>
    </div>
  </section>

</body>
</html>
```